Solar appointment reminder card

We are looking for a new design for our appointment reminder card since we have changed our logo. The card should have the new logo along with space for the employee to hand write the customers appointment date, time, the employees name and phone number.
I've uploaded what our old basic appointment card looked like and our new logo.

The cards should be in a standard business card size and could be horizontal or vertical.

```html
<!DOCTYPE html>
<html lang="en">
<head>
<meta charset="utf-8">
<title>Brightfield Solar – Appointment Card</title>
<link href="https://fonts.googleapis.com/css2?family=Arimo:wght@400;700&family=Montserrat:wght@800&display=swap" rel="stylesheet">
<style>
  :root {
    --bg-light: #cdced1;
    --bg-dark: #8a8a8e;
    --card-white: #ffffff;
    --card-black: #000000;
    --brand-orange: #f7941d;
    --brand-yellow: #ffc72c;
    --ink: #1a1a1a;
    --rule: #c8c8c8;
    --box-edge: #9a9a9a;
  }
  * { box-sizing: border-box; margin: 0; padding: 0; }
  html, body { width: 1200px; height: 1057px; overflow: hidden; }
  body {
    background: linear-gradient(90deg, var(--bg-light), var(--bg-dark));
    position: relative;
    font-family: "Arimo", Arial, sans-serif;
    color: var(--ink);
  }
  .card {
    position: absolute;
    width: 763px;
    height: 436px;
    border-radius: 0 65px 0 65px;
    overflow: hidden;
  }
  .card--front { left: 70px; top: 71px; background: var(--card-white); }
  .card--back  { left: 308px; top: 535px; background: var(--card-black); }

  .brand {
    position: absolute;
    display: flex;
    align-items: center;
    font-family: "Montserrat", sans-serif;
    font-weight: 800;
    color: var(--brand-orange);
    line-height: 0.95;
  }
  .brand__dot { border-radius: 50%; background: var(--brand-yellow); flex: none; }
  .brand--small { left: 0; right: 0; top: 48px; justify-content: center; gap: 14px; font-size: 34px; }
  .brand--small .brand__dot { width: 58px; height: 58px; }
  .brand--large { left: 0; right: 0; top: 150px; justify-content: center; gap: 26px; font-size: 64px; }
  .brand--large .brand__dot { width: 120px; height: 120px; }

  .title {
    position: absolute;
    left: 283px; width: 197px; top: 180px;
    text-align: center;
    font-weight: 700;
    font-size: 27px;
    color: var(--brand-orange);
    padding-bottom: 6px;
    border-bottom: 2px solid var(--brand-orange);
  }

  .days {
    position: absolute;
    left: 26px; top: 242px;
    display: flex;
    list-style: none;
  }
  .days__item {
    display: flex; align-items: center;
    width: 104px;
    font-size: 22px;
  }
  .days__box {
    width: 29px; height: 29px;
    border: 1.5px solid var(--box-edge);
    border-radius: 5px;
    margin-right: 9px;
  }

  .field {
    position: absolute;
    display: flex; align-items: flex-end;
    font-size: 21px;
    white-space: nowrap;
  }
  .field__line { border-bottom: 1.5px solid var(--rule); height: 1px; margin-left: 10px; margin-bottom: 3px; }
  .field--for   { left: 25px; top: 295px; }
  .field--for .field__line { width: 658px; }
  .field--date  { left: 25px; top: 337px; }
  .field--date .field__line { width: 233px; }
  .field--time  { left: 345px; top: 337px; }
  .field--time .field__line { width: 238px; }
  .field--ampm  { left: 667px; top: 335px; }
  .field--rep   { left: 25px; top: 378px; }
  .field--rep .field__line { width: 226px; }
  .field--phone { left: 428px; top: 378px; }
  .field--phone .field__line { width: 225px; }
</style>
</head>
<body>
  <section class="card card--front" aria-label="Appointment card front">
    <div class="brand brand--small">
      <span class="brand__dot"></span>
      <span class="brand__name">BRIGHTFIELD<br>SOLAR</span>
    </div>
    <h1 class="title">APPOINTMENT</h1>
    <ul class="days">
      <li class="days__item"><span class="days__box"></span>Mon</li>
      <li class="days__item"><span class="days__box"></span>Tue</li>
      <li class="days__item"><span class="days__box"></span>Wed</li>
      <li class="days__item"><span class="days__box"></span>Thu</li>
      <li class="days__item"><span class="days__box"></span>Fri</li>
      <li class="days__item"><span class="days__box"></span>Sat</li>
      <li class="days__item"><span class="days__box"></span>Sun</li>
    </ul>
    <div class="field field--for">For :<span class="field__line"></span></div>
    <div class="field field--date">Date :<span class="field__line"></span></div>
    <div class="field field--time">Time :<span class="field__line"></span></div>
    <div class="field field--ampm">AM/PM</div>
    <div class="field field--rep">Representative :<span class="field__line"></span></div>
    <div class="field field--phone">Phone :<span class="field__line"></span></div>
  </section>

  <section class="card card--back" aria-label="Appointment card back">
    <div class="brand brand--large">
      <span class="brand__dot"></span>
      <span class="brand__name">BRIGHTFIELD<br>SOLAR</span>
    </div>
  </section>
</body>
</html>
```